Derek Hollins Business card

Hey there, I’m hoping to have a business card designed. I’m in Real estate and just switched to a new Brokerage called: The Property Quarter

The back could just be the company name maybe or whatever looks good!

I’ve attached some logos of our company and some cards my buddy had done up.

On the card:
Derek Hollins
derekhollins@mailbox-demo.com
587-214-6093
derekhollins-demo.ca

Target Market(s)

Home buyers and sellers

Industry/Entity Type

Real Estate

Contact Information for Business Card

just looking for a cool and modern design with my picture on it. I like the idea of Black and red being used.

Requirements
Must have
• all the details provided. I'm open to anything. Just want a professional looking card.

```html
<!DOCTYPE html>
<html lang="en">
<head>
<meta charset="utf-8">
<title>Derek Hollins – Business Card</title>
<link href="https://fonts.googleapis.com/css2?family=Montserrat:wght@500;700;800&family=Open+Sans:wght@400;600&display=swap" rel="stylesheet">
<style>
  :root {
    --page: #141414;
    --card: #161616;
    --card-deep: #0d0d0d;
    --red: #e0223f;
    --white: #ffffff;
    --silver: #9a9a9a;
    --muted: #5a5a5a;
  }
  * { box-sizing: border-box; margin: 0; padding: 0; }
  html, body { width: 1200px; height: 977px; overflow: hidden; }
  body {
    background: var(--page);
    font-family: "Open Sans", sans-serif;
    position: relative;
  }
  .card {
    position: absolute;
    left: 220px;
    width: 760px;
    height: 434px;
    border-radius: 22px;
    background: linear-gradient(160deg, var(--card) 0%, var(--card-deep) 100%);
    border: 3px solid var(--red);
    overflow: hidden;
  }
  .card--front { top: 40px; }
  .card--back { top: 503px; }

  /* front */
  .front-mark {
    position: absolute; inset: 0;
    display: flex; flex-direction: column; align-items: center; justify-content: center;
  }
  .front-mark__name {
    font-family: "Montserrat", sans-serif;
    font-weight: 700;
    font-size: 54px;
    letter-spacing: 2px;
    color: var(--silver);
  }
  .front-mark__tagline {
    margin-top: 10px;
    display: flex; align-items: center; gap: 12px;
    font-size: 15px; letter-spacing: 4px;
    color: var(--muted);
  }
  .front-mark__tagline::before,
  .front-mark__tagline::after {
    content: ""; width: 50px; height: 1px; background: var(--muted);
  }

  /* back */
  .photo {
    position: absolute; left: 70px; top: 28px;
    width: 240px; height: 218px;
    background: radial-gradient(ellipse at 50% 40%, #3a3a3c 0%, #232325 55%, transparent 80%);
  }
  .brand {
    position: absolute; right: 70px; top: 60px;
    display: flex; flex-direction: column; align-items: flex-end;
  }
  .brand__name {
    font-family: "Montserrat", sans-serif;
    font-weight: 700; font-size: 40px; letter-spacing: 1px;
    color: var(--white);
  }
  .brand__tagline {
    margin-top: 6px;
    display: flex; align-items: center; gap: 10px;
    font-size: 12px; letter-spacing: 3px; color: var(--white);
  }
  .brand__tagline::before { content: ""; width: 40px; height: 1px; background: var(--white); }

  .brokerage {
    position: absolute; right: 70px; top: 205px;
    display: flex; align-items: center; gap: 12px;
  }
  .brokerage__dot { width: 18px; height: 18px; background: var(--red); }
  .brokerage__name {
    font-family: "Montserrat", sans-serif;
    font-weight: 800; font-size: 24px; color: var(--white);
  }

  .agent {
    position: absolute; left: 70px; right: 70px; top: 248px;
  }
  .agent__name {
    font-family: "Montserrat", sans-serif;
    font-weight: 800; font-size: 30px; line-height: 36px;
    color: var(--red); letter-spacing: .5px;
  }
  .agent__role-row {
    display: flex; align-items: center; gap: 10px;
    margin-top: 2px;
  }
  .agent__role {
    font-size: 17px; line-height: 22px; color: var(--white); letter-spacing: 1px;
  }
  .agent__divider {
    flex: 1; height: 1px; background: var(--white);
  }

  .contacts {
    position: absolute; left: 74px; top: 322px;
    list-style: none;
  }
  .contacts li {
    display: flex; align-items: center; gap: 14px;
    font-size: 17px; color: var(--white); line-height: 26px;
  }
  .contacts svg { width: 16px; height: 16px; fill: var(--red); flex: none; }
</style>
</head>
<body>

<section class="card card--front" aria-label="Card front">
  <div class="front-mark">
    <div class="front-mark__name">DEREK HOLLINS</div>
    <div class="front-mark__tagline">THE PROPERTY QUARTER</div>
  </div>
</section>

<section class="card card--back" aria-label="Card back">
  <div class="photo" role="img" aria-label="Portrait photo of Derek Hollins in a dark suit"></div>

  <div class="brand">
    <div class="brand__name">DEREK HOLLINS</div>
    <div class="brand__tagline">THE PROPERTY QUARTER</div>
  </div>

  <div class="brokerage">
    <span class="brokerage__dot"></span>
    <span class="brokerage__name">THE PROPERTY QUARTER</span>
  </div>

  <div class="agent">
    <div class="agent__name">DEREK HOLLINS</div>
    <div class="agent__role-row">
      <span class="agent__role">REALTOR</span>
      <span class="agent__divider"></span>
    </div>
  </div>

  <ul class="contacts">
    <li>
      <svg viewBox="0 0 24 24" aria-hidden="true"><path d="M6.6 10.8a15.1 15.1 0 0 0 6.6 6.6l2.2-2.2c.3-.3.7-.4 1-.2 1.1.4 2.3.6 3.6.6.6 0 1 .4 1 1V20c0 .6-.4 1-1 1A17 17 0 0 1 3 4c0-.6.4-1 1-1h3.5c.6 0 1 .4 1 1 0 1.3.2 2.5.6 3.6.1.3 0 .7-.2 1z"/></svg>
      587-214-6093
    </li>
    <li>
      <svg viewBox="0 0 24 24" aria-hidden="true"><path d="M2 5h20v14H2z M3 6l9 7 9-7" stroke="#161616" stroke-width="1.5"/></svg>
      derekhollins@mailbox-demo.com
    </li>
    <li>
      <svg viewBox="0 0 24 24" aria-hidden="true"><circle cx="12" cy="12" r="10"/><path d="M2 12h20M12 2c3 3 3 17 0 20M12 2c-3 3-3 17 0 20" stroke="#161616" stroke-width="1.5" fill="none"/></svg>
      derekhollins-demo.ca
    </li>
  </ul>
</section>

</body>
</html>
```